Design mobile friendly real estate and property management company landing page

Design a clean, crisp modern looking landing page that is mobile-friendly (must resize, preferably using bootstrap framework). Landing page will consist of heading with login area, company info, body consists of company description and services, a list of available rental properties with photos, and a footer with additional links and info. Working on updating with text for text areas marked A, B, and C on the layout pdf, but in meantime, lorem ipsum is fine. I can connect events to most buttons, etc. Just need the bootstrap and html functionality set up. Previous company website (which should not be relied upon) is www.kbtq.net This is somewhat of a template for a start, but looking for a more professional and modern design for the new website. But this gives an idea of the content and what needs to be displayed, and how.

Target Market(s)

Clients looking for a property management company that is efficient and well-organized.

Industry/Entity Type

Property Management

Coding

Coded - Design and coding required

Number of Pages Required

1 page

Font styles to use
Sans Serif

Colors
0355a3

Requirements
Must have
• Resize for the screen using bootstrap.
• Navigation that collapses for mobile devices
• Large text boxes and good solid spacing around all elements.
Nice to have
• for property images it would be nice if they can be swiped on touch enabled devices (to the next or previous image). And have navigation that can be clicked to next or previous images.
• Would be nice if a captcha verification was included on contact form.
Should not have
• Fancy or eccentric art

```html
<!DOCTYPE html>
<html lang="en">
<head>
<meta charset="utf-8">
<title>Brightwell Property Services</title>
<link rel="stylesheet" href="https://fonts.googleapis.com/css2?family=Cinzel:wght@400;700&family=Lato:ital,wght@0,400;0,700;1,400&display=swap">
<style>
:root{
  --brand:#0355a3;
  --brand-dark:#02427f;
  --ink:#111111;
  --text:#222222;
  --muted:#666666;
  --line:#d9d9d9;
  --pale:#eeeeee;
  --footer:#2b2b2b;
  --white:#ffffff;
}
*{box-sizing:border-box;margin:0;padding:0}
html,body{width:1200px;height:2765px;overflow:hidden}
body{position:relative;background:var(--white);font-family:"Lato",Arial,sans-serif;color:var(--text)}
.abs{position:absolute}
.display{font-family:"Cinzel",Georgia,serif}

/* top bar */
.topbar{left:0;top:0;width:1200px;height:37px;background:var(--ink);color:var(--white);font-size:15px;display:flex;align-items:center;padding-left:81px;gap:40px}
.topbar span{display:flex;align-items:center;gap:10px}
.login{left:1023px;top:0;width:96px;height:37px;background:var(--brand);color:var(--white);display:flex;align-items:center;justify-content:center;gap:8px;font-size:16px}

/* header */
.brand-name{left:81px;top:78px;display:flex;align-items:center;gap:12px;color:var(--ink);font-family:"Cinzel",Georgia,serif;font-weight:700;font-size:27px;line-height:1}
.brand-name .mark{width:16px;height:16px;background:var(--ink);flex:none}
.weather{left:774px;top:52px;width:345px;height:81px;border:1px solid var(--line);background:#fafafa}
.weather .city{position:absolute;left:8px;top:6px;font-size:15px;font-weight:700;color:#333}
.weather .temp{position:absolute;left:10px;top:30px;display:flex;align-items:center;gap:6px;font-size:36px;color:#777}
.weather .today{font-size:12px;color:#555;line-height:1.2}
.weather .days{position:absolute;left:180px;top:30px;display:flex;gap:14px;font-size:9px;color:#777;text-align:center}

/* nav */
.nav{left:0;top:151px;width:1200px;height:44px;background:var(--brand);display:flex;padding-left:81px}
.nav a{display:flex;align-items:center;justify-content:center;height:44px;color:var(--white);text-decoration:none;font-family:"Cinzel",Georgia,serif;font-size:16px;letter-spacing:1px;border-right:1px solid rgba(255,255,255,.25)}
.nav a.active{background:var(--ink)}

/* hero */
.hero{left:0;top:195px;width:1200px;height:472px;background:linear-gradient(100deg,#a89a8c 0%,#cdbfb3 30%,#9a9aa0 60%,#5c6470 100%)}
.hero-caption{left:0;top:555px;width:1200px;text-align:center;color:var(--white);font-size:34px;line-height:44px;text-shadow:0 2px 4px rgba(0,0,0,.5)}
.arrow-tab{top:388px;width:44px;height:44px;background:var(--white);display:flex;align-items:center;justify-content:center}

/* section headings */
.heading{width:1200px;left:0;text-align:center;font-size:35px;font-weight:700;letter-spacing:0}
.divider{left:326px;width:548px;height:20px;display:flex;align-items:center;gap:10px}
.divider i{flex:1;height:1px;background:var(--line)}

/* welcome */
.welcome-text{left:103px;top:800px;width:995px;text-align:center;font-size:14px;line-height:24px;color:#222}
.welcome-text a{color:var(--brand);text-decoration:none}
.callbox{left:243px;top:955px;width:714px;height:70px;border:1px solid #ccc;border-radius:10px;background:#f6f6f6;box-shadow:0 3px 6px rgba(0,0,0,.12);display:flex;align-items:center;justify-content:center;gap:16px;font-size:32px;color:#222}
.callbox strong{color:var(--brand);font-weight:700}

/* services */
.services{left:0;top:1093px;width:1200px;height:417px;background:var(--brand)}
.service{top:1262px;width:240px;text-align:center;color:var(--white)}
.service .circle{margin:0 auto;width:104px;height:104px;border-radius:50%;background:var(--ink);border:4px solid var(--white);display:flex;align-items:center;justify-content:center}
.service h3{font-family:"Cinzel",Georgia,serif;font-weight:700;font-size:19px;line-height:25px;margin-top:19px;letter-spacing:1px}
.service p{font-size:13px;line-height:18px;margin-top:9px}
.service .plus{margin:10px auto 0;width:16px;height:16px;background:var(--ink);color:var(--white);font-size:14px;line-height:16px}

/* properties */
.card{top:1662px;width:240px;height:304px;border:1px solid var(--line);background:var(--white);box-shadow:0 1px 3px rgba(0,0,0,.08)}
.card .photo{margin:8px;height:133px}
.card h4{font-family:"Cinzel",Georgia,serif;font-weight:700;font-size:15px;margin:12px 10px 0}
.card .desc{font-size:12px;color:var(--muted);margin:4px 10px 0}
.card .row{display:flex;justify-content:space-between;align-items:center;margin:16px 10px 0}
.card .tag{background:var(--ink);color:var(--white);font-size:13px;padding:5px 10px}
.card .price{font-size:24px;font-weight:700;color:#111}
.card .meta{position:absolute;left:0;bottom:0;width:100%;height:40px;border-top:1px solid var(--line);display:flex;font-size:11px;color:#555}
.card .meta span{flex:1;display:flex;align-items:center;justify-content:center;gap:5px;border-right:1px solid var(--line)}
.card .meta span:last-child{border-right:0}

/* testimonials */
.testimonials{left:0;top:2033px;width:1200px;height:298px;background:var(--pale)}
.avatar{left:103px;top:2184px;width:80px;height:80px;border-radius:50%;border:3px solid var(--brand);background:linear-gradient(#c7d4e2,#8ea4bc)}
.quote{left:217px;top:2188px;width:911px;font-size:13px;line-height:22px;font-style:italic;color:#222}
.quote .mark{font-size:24px;color:#999;font-style:normal;line-height:0;vertical-align:-4px}
.quote-author{left:219px;top:2270px;font-size:15px;font-weight:700;color:#333}

/* newsletter */
.newsletter{left:0;top:2331px;width:1200px;height:98px;background:linear-gradient(180deg,#0d66bd,#02468a)}
.news-icon{left:81px;top:2358px;width:48px;height:48px;border-radius:50%;border:2px solid var(--white);background:var(--ink);display:flex;align-items:center;justify-content:center}
.news-title{left:151px;top:2362px;font-family:"Cinzel",Georgia,serif;font-weight:700;font-size:26px;color:var(--white);letter-spacing:1px;display:flex;align-items:center;gap:16px}
.news-input{left:498px;top:2364px;width:452px;height:40px;background:var(--white);font-size:13px;padding-left:12px;line-height:40px;color:#222}
.news-btn{left:966px;top:2364px;width:153px;height:40px;background:var(--ink);color:var(--white);font-size:17px;font-weight:700;text-align:center;line-height:40px}

/* footer */
.footer{left:0;top:2429px;width:1200px;height:291px;background:var(--footer)}
.fcol{top:2449px;color:var(--white)}
.fcol h5{font-family:"Cinzel",Georgia,serif;font-weight:700;font-size:17px;letter-spacing:1px;padding-bottom:10px;border-bottom:1px solid #444;margin-bottom:12px}
.fcol ul{list-style:none;font-size:13px}
.fcol li{line-height:26.5px}
.fcol li::before{content:"›";margin-right:8px}
.field{background:var(--white);color:#222;font-size:12px;padding:8px 10px;margin-bottom:9px;height:32px}
.field.tall{height:62px}
.submit{background:var(--brand);color:var(--white);font-size:14px;font-weight:700;width:80px;height:32px;text-align:center;line-height:32px}
.contact-row{display:flex;gap:16px;align-items:flex-start;font-size:13px;line-height:19px;margin-bottom:32px}
.contact-row .ic{width:30px;height:30px;background:var(--brand);display:flex;align-items:center;justify-content:center;flex:none}
.copyright{left:0;top:2720px;width:1200px;height:45px;background:var(--brand);color:var(--white);font-size:13px;text-align:center;line-height:45px}
</style>
</head>
<body>

<div class="abs topbar">
  <span><svg width="16" height="16" viewBox="0 0 24 24" fill="#fff"><path d="M6.6 10.8a15 15 0 0 0 6.6 6.6l2.2-2.2c.3-.3.7-.4 1-.2 1.1.4 2.3.6 3.6.6.6 0 1 .4 1 1V20c0 .6-.4 1-1 1A17 17 0 0 1 3 4c0-.6.4-1 1-1h3.5c.6 0 1 .4 1 1 0 1.3.2 2.5.6 3.6.1.3 0 .7-.2 1z"/></svg>123-456-7890</span>
  <span><svg width="16" height="12" viewBox="0 0 16 12"><rect width="16" height="12" fill="#fff"/><path d="M0 0l8 6 8-6" stroke="#111" fill="none"/></svg>info@brightwellproperty.com</span>
</div>
<div class="abs login"><svg width="16" height="16" viewBox="0 0 16 16" fill="none" stroke="#fff" stroke-width="1.6"><path d="M9 2h5v12H9M2 8h8M7 5l3 3-3 3"/></svg>Login</div>

<div class="abs brand-name"><span class="mark"></span>Brightwell Property Services</div>

<div class="abs weather">
  <div class="city">PERTH WEATHER</div>
  <div class="temp">
    <svg width="34" height="34" viewBox="0 0 34 34"><circle cx="17" cy="17" r="8" fill="#f5a623"/><g stroke="#f5a623" stroke-width="2"><path d="M17 1v5M17 28v5M1 17h5M28 17h5M5.7 5.7l3.5 3.5M24.8 24.8l3.5 3.5M5.7 28.3l3.5-3.5M24.8 9.2l3.5-3.5"/></g></svg>
    26°C <span class="today">Today<br>Cloudy</span>
  </div>
  <div class="days">
    <div><svg width="22" height="16"><circle cx="11" cy="8" r="6" fill="#f5a623"/></svg><br>MON<br>18°-20°</div>
    <div><svg width="22" height="16"><circle cx="11" cy="8" r="6" fill="#f5a623"/></svg><br>TUE<br>28°-30°</div>
    <div><svg width="22" height="16"><circle cx="8" cy="7" r="5" fill="#f5a623"/><ellipse cx="14" cy="11" rx="7" ry="4" fill="#8fb6d9"/></svg><br>WED<br>20°-23°</div>
    <div><svg width="22" height="16"><circle cx="11" cy="8" r="6" fill="#f5a623"/></svg><br>THU<br>26°-31°</div>
  </div>
</div>

<nav class="abs nav">
  <a class="active" style="width:100px">HOME</a>
  <a style="width:150px">ABOUT US</a>
  <a style="width:150px">SERVICES</a>
  <a style="width:142px">FOR SALE</a>
  <a style="width:144px">FOR RENT</a>
  <a style="width:188px">TESTIMONIALS</a>
  <a style="width:164px;border-right:0">CONTACT US</a>
</nav>

<div class="abs hero" role="img" aria-label="Photo of a hand holding a small model house and a set of keys"></div>
<div class="abs hero-caption">We Are Professional Property Management Company Committed<br>To Take Care Of Your Property When It Is Vacant</div>
<div class="abs arrow-tab" style="left:0"><svg width="14" height="20"><path d="M11 2L3 10l8 8" stroke="#0355a3" stroke-width="3" fill="none"/></svg></div>
<div class="abs arrow-tab" style="left:1156px"><svg width="14" height="20"><path d="M3 2l8 8-8 8" stroke="#0355a3" stroke-width="3" fill="none"/></svg></div>

<h1 class="abs heading display" style="top:714px;color:var(--ink)">WELCOME TO BRIGHTWELL PROPERTY SERVICES</h1>
<div class="abs divider" style="top:769px"><i></i><svg width="18" height="16" viewBox="0 0 18 16"><path d="M9 1L1 8h2v7h12V8h2z" fill="#cfcfcf"/></svg><i></i></div>
<p class="abs welcome-text">Lorem ipsum dolor sit amet, consectetuer adipiscing elit, sed diam nonummy nibh euismod tincidunt ut laoreet dolore magna aliquam erat volutpat. Ut wisi enim ad minim veniam, quis nostrud exerci tation ullamcorper suscipit lobortis nisl ut aliquip ex ea commodo consequat. Duis autem vel eum iriure dolor in hendrerit in vulputate velit esse molestie consequat, vel illum dolore eu feugiat nulla facilisis at vero eros et accumsan et iusto odio dignissim qui blandit praesent luptatum zzril delenit augue duis dolore te feugait nulla facilisi. <a>Read More..</a></p>
<div class="abs callbox">
  <svg width="36" height="36" viewBox="0 0 36 36"><circle cx="18" cy="18" r="16" fill="none" stroke="#0355a3" stroke-width="2"/><path d="M12 10c-2 2-1 7 3 11s9 5 11 3l-3-4-3 2c-2-1-4-3-5-5l2-3z" fill="#0355a3"/></svg>
  <span>Call Now &amp; Speak Directly - <strong>123 - 456 -7890</strong></span>
</div>

<section class="abs services"></section>
<h2 class="abs heading display" style="top:1138px;color:var(--white)">OUR SERVICES</h2>
<div class="abs divider" style="top:1190px"><i style="background:rgba(255,255,255,.3)"></i><svg width="18" height="16" viewBox="0 0 18 16"><path d="M9 1L1 8h2v7h12V8h2z" fill="#9cc0e6"/></svg><i style="background:rgba(255,255,255,.3)"></i></div>
<svg class="abs" style="left:55px;top:1398px" width="14" height="22"><path d="M11 2L3 11l8 9" stroke="#fff" stroke-width="2" fill="none"/></svg>
<svg class="abs" style="left:1128px;top:1398px" width="14" height="22"><path d="M3 2l8 9-8 9" stroke="#fff" stroke-width="2" fill="none"/></svg>

<div class="abs service" style="left:79px">
  <div class="circle"><svg width="44" height="44" viewBox="0 0 44 44" fill="#fff"><rect x="8" y="6" width="28" height="34"/><g fill="#111"><rect x="13" y="11" width="5" height="5"/><rect x="20" y="11" width="5" height="5"/><rect x="27" y="11" width="5" height="5"/><rect x="13" y="19" width="5" height="5"/><rect x="20" y="19" width="5" height="5"/><rect x="27" y="19" width="5" height="5"/><rect x="19" y="30" width="7" height="10"/></g></svg></div>
  <h3>Apartment<br>Management</h3>
  <p>Lorem ipsum dolor sit amet sect<br>etmo adipiscing elit sed Lore</p>
  <div class="plus">+</div>
</div>
<div class="abs service" style="left:350px">
  <div class="circle"><svg width="46" height="44" viewBox="0 0 46 44" fill="#fff"><path d="M23 4L4 20h5v18h28V20h5z"/><rect x="19" y="26" width="8" height="12" fill="#111"/><rect x="6" y="30" width="34" height="4" fill="#fff" transform="rotate(-20 23 32)"/></svg></div>
  <h3>Foreclosure<br>Management</h3>
  <p>Lorem ipsum dolor sit amet sect<br>etmo adipiscing elit sed Lore</p>
  <div class="plus">+</div>
</div>
<div class="abs service" style="left:619px">
  <div class="circle"><svg width="46" height="44" viewBox="0 0 46 44" fill="#fff"><path d="M23 6L4 22h5v16h28V22h5z"/><rect x="14" y="24" width="6" height="6" fill="#111"/><rect x="26" y="24" width="6" height="6" fill="#111"/></svg></div>
  <h3>Homeowner<br>Association</h3>
  <p>Lorem ipsum dolor sit amet sect<br>etmo adipiscing elit sed Lore</p>
  <div class="plus">+</div>
</div>
<div class="abs service" style="left:890px">
  <div class="circle"><svg width="46" height="44" viewBox="0 0 46 44" fill="#fff"><path d="M23 4L4 20h5v18h28V20h5z"/><path d="M23 14a5 5 0 1 1 0 10 5 5 0 0 1 0-10zm-9 22c0-6 4-9 9-9s9 3 9 9z" fill="#111"/></svg></div>
  <h3>Condominium<br>Management</h3>
  <p>Lorem ipsum dolor sit amet sect<br>etmo adipiscing elit sed Lore</p>
  <div class="plus">+</div>
</div>

<h2 class="abs heading display" style="top:1560px;color:var(--ink)">FEATURED PROPERTIES</h2>
<div class="abs divider" style="top:1615px"><i></i><svg width="18" height="16" viewBox="0 0 18 16"><path d="M9 1L1 8h2v7h12V8h2z" fill="#cfcfcf"/></svg><i></i></div>

<div class="abs card" style="left:83px">
  <div class="photo" role="img" aria-label="Photo of a large brick family house with a lawn" style="background:linear-gradient(#6fa4dc 0%,#8fb7e0 35%,#9b5a3f 55%,#5d8a3a 100%)"></div>
  <h4>123 DOLLAR SMIT AMET</h4><p class="desc">Lorem ipsum dolor sit amet, consecteti</p>
  <div class="row"><span class="tag">For Rent</span><span class="price">$ 123</span></div>
  <div class="meta"><span>⤢ 1200 sq ft</span><span>▭ 2 Beds</span><span>◔ 2 Baths</span></div>
</div>
<div class="abs card" style="left:350px">
  <div class="photo" role="img" aria-label="Photo of a grey stone suburban house" style="background:linear-gradient(#9fc3e6 0%,#c4d4e2 35%,#7b7f84 60%,#6b8f4a 100%)"></div>
  <h4>123 DOLLAR SMIT AMET</h4><p class="desc">Lorem ipsum dolor sit amet, consecteti</p>
  <div class="row"><span class="tag">For Sell</span><span class="price">$ 123</span></div>
  <div class="meta"><span>⤢ 1200 sq ft</span><span>▭ 2 Beds</span><span>◔ 2 Baths</span></div>
</div>
<div class="abs card" style="left:614px">
  <div class="photo" role="img" aria-label="Photo of a dark house with a white picket fence" style="background:linear-gradient(#bcd3e8 0%,#a06a55 30%,#4a4a5a 60%,#d9d9d9 100%)"></div>
  <h4>123 DOLLAR SMIT AMET</h4><p class="desc">Lorem ipsum dolor sit amet, consecteti</p>
  <div class="row"><span class="tag">For Rent</span><span class="price">$ 523</span></div>
  <div class="meta"><span>⤢ 1200 sq ft</span><span>▭ 2 Beds</span><span>◔ 2 Baths</span></div>
</div>
<div class="abs card" style="left:880px">
  <div class="photo" role="img" aria-label="Photo of a modern white concrete house" style="background:linear-gradient(#b8c7d2 0%,#d8d6cc 40%,#c9c4b5 65%,#6f8a4c 100%)"></div>
  <h4>123 DOLLAR SMIT AMET</h4><p class="desc">Lorem ipsum dolor sit amet, consecteti</p>
  <div class="row"><span class="tag">For Sell</span><span class="price">$ 320</span></div>
  <div class="meta"><span>⤢ 1200 sq ft</span><span>▭ 2 Beds</span><span>◔ 2 Baths</span></div>
</div>

<section class="abs testimonials"></section>
<h2 class="abs heading display" style="top:2080px;color:var(--ink)">CLIENT&nbsp; TESTIMONIALS</h2>
<div class="abs divider" style="top:2135px"><i></i><svg width="18" height="16" viewBox="0 0 18 16"><path d="M9 1L1 8h2v7h12V8h2z" fill="#cfcfcf"/></svg><i></i></div>
<div class="abs avatar" role="img" aria-label="Client portrait"></div>
<p class="abs quote"><span class="mark">“</span> Lorem ipsdolor sit amet, consectetur adipiscing elit. Donec sit amet nulla vitae tortor iaculis commodo. Nulla interdum dui vitae lectus malesuada ac dignissim mi vehicula. Nullam ornare vulputate sem vitae convallis. Proin et faucibus eros. Nam id rutrum risus, quis eleifend tortor. Nulla scelerisque vitae ante vitae,rhoncus pellentesque turpis. Donec feugiat malesuada justo, quis porta urna egestas nec. Duis nec lobortis justo, ac varius ante. <span class="mark">”</span></p>
<div class="abs quote-author">Mr. Daren Holt</div>
<svg class="abs" style="left:1088px;top:2266px" width="32" height="14"><path d="M8 2L3 7l5 5" stroke="#111" stroke-width="2" fill="none"/><path d="M24 2l5 5-5 5" stroke="#0355a3" stroke-width="2" fill="none"/></svg>

<section class="abs newsletter"></section>
<div class="abs news-icon"><svg width="22" height="16" viewBox="0 0 22 16"><rect width="22" height="16" fill="#fff"/><path d="M0 0l11 8 11-8" stroke="#111" fill="none"/></svg></div>
<div class="abs news-title">Newsletter Signup <svg width="14" height="28"><path d="M2 2l10 12-10 12" stroke="#fff" stroke-width="2" fill="none"/></svg></div>
<div class="abs news-input">Your E-mail</div>
<div class="abs news-btn">SIGN UP</div>

<footer class="abs footer"></footer>
<div class="abs fcol" style="left:81px;width:160px">
  <h5>NAVIGATION</h5>
  <ul><li>Home</li><li>About Us</li><li>Services</li><li>For Sale</li><li>For Rent</li><li>Testimonials</li><li>Contact Us</li></ul>
</div>
<div class="abs fcol" style="left:310px;width:160px">
  <h5>OTHER LINKS</h5>
  <ul><li>Loren ipsum dolor</li><li>Dapibus eget eleme</li><li>Utm tellus dolor</li><li>Velmki cursu itas</li><li>Fir mnbvcd sirdcnc</li></ul>
</div>
<div class="abs fcol" style="left:538px;width:267px">
  <h5 style="border:0">QUICK CONTACT</h5>
  <div class="field">Name</div>
  <div class="field">Email</div>
  <div class="field tall">Your message</div>
  <div class="submit">SUBMIT</div>
</div>
<div class="abs fcol" style="left:874px;width:245px">
  <h5>GET IN TOUCH</h5>
  <div class="contact-row"><span class="ic"><svg width="14" height="18" viewBox="0 0 14 18"><path d="M7 0a7 7 0 0 1 7 7c0 5-7 11-7 11S0 12 0 7a7 7 0 0 1 7-7z" fill="#fff"/><circle cx="7" cy="7" r="2.5" fill="#0355a3"/></svg></span><span><b>Brightwell Property Services</b><br>1234 Lren Ipsum dolor suit<br>Nbcdere, IL 1234</span></div>
  <div class="contact-row"><span class="ic"><svg width="14" height="14" viewBox="0 0 24 24" fill="#fff"><path d="M6.6 10.8a15 15 0 0 0 6.6 6.6l2.2-2.2c.3-.3.7-.4 1-.2 1.1.4 2.3.6 3.6.6.6 0 1 .4 1 1V20c0 .6-.4 1-1 1A17 17 0 0 1 3 4c0-.6.4-1 1-1h3.5c.6 0 1 .4 1 1 0 1.3.2 2.5.6 3.6.1.3 0 .7-.2 1z"/></svg></span><span style="line-height:30px">123-456-7890</span></div>
  <div class="contact-row"><span class="ic"><svg width="16" height="12" viewBox="0 0 16 12"><rect width="16" height="12" fill="#fff"/><path d="M0 0l8 6 8-6" stroke="#0355a3" fill="none"/></svg></span><span style="line-height:30px">info@brightwellproperty.com</span></div>
</div>
<div class="abs copyright">Copyright © 2016 Brightwell Property Services&nbsp; | &nbsp;All Rights Reserved.</div>

</body>
</html>
```